Dentistry on Brackwell Marketing Brochure

I require a brochure to market our practice and to send to new patients after they have made initial phone contact, in our 'new patient package' .
My preference is for a double sided A4 trifold brochure.
Please find attached the style guide and information to be included.
Also, please visit our website at www.dentistryonbrackwell.com.au to get an idea of our brand- we prefer a clean, fresh look that still conveys warmth and professionalism.
The images from our website can be used for the brochure.
Please include the map attached.
Industry/Entity Type
Marketing
Look and feel
Each slider illustrates characteristics of the customer's brand and the style your logo design should communicate.

```html
<!DOCTYPE html>
<html lang="en">
<head>
<meta charset="utf-8">
<title>Dentistry On Brackwell – Welcome</title>
<link href="https://fonts.googleapis.com/css2?family=Open+Sans:wght@300;400&family=Playfair+Display:ital,wght@1,400&display=swap" rel="stylesheet">
<style>
  :root {
    --brand-green: #b8cb0a;
    --heading-green: #a9bd14;
    --body-grey: #6e6f71;
    --stripe: #eceeef;
    --paper: #ffffff;
  }
  * { margin: 0; padding: 0; box-sizing: border-box; }
  html, body { width: 849px; height: 1200px; overflow: hidden; background: var(--paper); }
  .page { position: relative; width: 849px; height: 1200px; overflow: hidden; background: var(--paper);
    font-family: "Open Sans", Arial, sans-serif; font-weight: 300; color: var(--body-grey); }

  .stripes { position: absolute; left: 0; top: 0; width: 180px; height: 250px;
    background: repeating-linear-gradient(to bottom, var(--paper) 0 6px, var(--stripe) 6px 9px); }
  .team-photo { position: absolute; left: 180px; top: 0; width: 669px; height: 250px;
    background: linear-gradient(100deg, #e9ecec 0%, #d9dcd6 35%, #c9d07a 60%, #dfe3e2 100%); }

  .welcome-band { position: absolute; left: 0; top: 250px; width: 849px; height: 94px; background: var(--brand-green); }
  .welcome-band h1 { position: absolute; left: 65px; top: 12px; font-family: "Playfair Display", Georgia, serif;
    font-style: italic; font-weight: 400; font-size: 54px; color: var(--paper); letter-spacing: 0.5px; }

  .intro { position: absolute; left: 61px; top: 371px; width: 392px; font-size: 12.7px; line-height: 17.1px; }
  .intro p { margin-bottom: 17.1px; }

  .section-title { font-family: "Playfair Display", Georgia, serif; font-style: italic; font-weight: 400;
    color: var(--heading-green); font-size: 25px; letter-spacing: 1.2px; line-height: 1; }

  .services { position: absolute; left: 61px; top: 770px; width: 400px; }
  .services .section-title { margin-bottom: 18px; }
  .services-list { position: relative; font-size: 12.7px; line-height: 17.1px; }
  .services-list ul { list-style: none; position: absolute; top: 0; }
  .services-list .col-a { left: 20px; }
  .services-list .col-b { left: 222px; }
  .services-list li { position: relative; white-space: nowrap; }
  .services-list li.bulleted { padding-left: 20px; }
  .services-list li.bulleted::before { content: "•"; position: absolute; left: 0; font-size: 9px; }

  .children { position: absolute; left: 485px; top: 365px; width: 310px; font-size: 12.7px; line-height: 17.1px; }
  .children .section-title { margin-bottom: 14px; }
  .children p { margin-bottom: 17.1px; }
  .children .days-title { margin-top: 4px; }
  .children .note { line-height: 13.5px; }

  .photo-implant { position: absolute; left: 0; top: 949px; width: 465px; height: 251px;
    background: linear-gradient(120deg, #dfe6ea 0%, #b9c8d8 40%, #8f9aa2 75%, #6c6660 100%); }
  .photo-child { position: absolute; left: 465px; top: 949px; width: 384px; height: 251px;
    background: linear-gradient(110deg, #e8ecee 0%, #d8c2ad 40%, #c9d64f 75%, #3a3a3c 100%); }
</style>
</head>
<body>
<div class="page">
  <div class="stripes"></div>
  <div class="team-photo" role="img" aria-label="Dental team standing and seated on a green patterned couch in the practice"></div>

  <div class="welcome-band"><h1>Welcome</h1></div>

  <div class="intro">
    <p>At Dentistry On Brackwell we offer an advanced standard of dental care services, using the most current philosophies and techniques. Our practitioners personalise dental care to your individual requirements, not only caring for your teeth and gums, but also caring about your general health and wellbeing.</p>
    <p>We understand that dentistry is about so much more than just healthy teeth and gums. It’s also about how you function, your appearance and most importantly, how you feel- giving you confidence to be yourself!</p>
    <p>Our aim is to create and maintain sustainable healthy mouths for life, allowing you to feel comfortable and confident. This is achieved by our commitment to high quality, long lasting dental solutions when required and using preventive solutions for long term stability. Our caring, gentle dentists will take the time to listen to your concerns and help you to achieve your dental goals.</p>
    <p>We are so proud to be able to serve you with a comfortable, state-of-the-art facility and an award winning dental team who have been selected as the most caring, professional and highly respected in their field.</p>
  </div>

  <div class="services">
    <h2 class="section-title">Our services include:</h2>
    <div class="services-list">
      <ul class="col-a">
        <li>Digital radiographs &amp; OPGs</li>
        <li>CERAFIT ceramic restorations</li>
        <li>Sedation dentistry</li>
        <li class="bulleted">Dental implants</li>
        <li class="bulleted">Root canal therapy</li>
        <li class="bulleted">Crown and bridge</li>
      </ul>
      <ul class="col-b">
        <li class="bulleted">Hygiene care</li>
        <li class="bulleted">Veneers</li>
        <li class="bulleted">Whitening</li>
        <li class="bulleted">Gum treatment</li>
        <li class="bulleted">Mouthguards</li>
        <li class="bulleted">Children’s dental care</li>
      </ul>
    </div>
  </div>

  <div class="children">
    <h2 class="section-title">Child and Teen Dental</h2>
    <p>Dental decay rates are rapidly rising. To ensure our young patients have optimum dental health for life, Dentistry on Brackwell is investing more time and effort into the care of our children and teenage patients. Our oral health therapists are our children’s dental program practitioners, as they are specifically trained in children’s dental care.</p>
    <p>Our OHTs have a special interest in the prevention of dental disease throughout the lifespan. They will provide you with the most current advice and product recommendations to suit your individual needs. They are specifically focused on giving your child the best head start they need to maintain a healthy smile for life.</p>
    <h2 class="section-title days-title">Children’s Dental Days</h2>
    <p style="margin-top:14px">Our children’s days are fantastic for young children who haven’t been to the dentist before or are shy or nervous about going to the dentist. This is a fun day where children can have their face painted, put on dress ups, get their teeth checked and go home with lots of rewards, a happy smile and a positive dental experience!</p>
    <p class="note">Photos from our previous children’s days are available on the Dentistry On Brackwell Friendbook page.</p>
  </div>

  <div class="photo-implant" role="img" aria-label="Dentist pointing at a tooth restoration design on a screen beside a seated patient"></div>
  <div class="photo-child" role="img" aria-label="Smiling dentist showing a young girl a model of teeth"></div>
</div>
</body>
</html>
```